Amber Hollow Productions

I need a business card design for a new freelance film production company using or incorporating the logo:
I want the card to be creative, minimal, yet professional. Feel free to use a variety of different shapes and sizes/ textures for the card.

Industry/Entity Type

Film Production

```html
<!DOCTYPE html>
<html lang="en">
<head>
<meta charset="utf-8">
<title>Amber Hollow Productions – Business Card</title>
<link href="https://fonts.googleapis.com/css2?family=Open+Sans:wght@400;600;700&display=swap" rel="stylesheet">
<style>
  :root {
    --brand-blue: #0f4b9c;
    --ink: #1e1f24;
    --steel: #8a8d92;
    --steel-dark: #6e7175;
    --paper: #f1f1f1;
    --stage: #e6e7e9;
    --divider: #d6d7d9;
    --white: #ffffff;
  }
  * { box-sizing: border-box; margin: 0; padding: 0; }
  html, body {
    width: 1200px; height: 955px; overflow: hidden;
    background: var(--stage);
    font-family: "Open Sans", Arial, sans-serif;
  }
  .canvas { position: relative; width: 1200px; height: 955px; }
  .card {
    position: absolute; left: 220px; width: 760px; height: 434px;
    box-shadow: 0 6px 18px rgba(0,0,0,.12);
    overflow: hidden;
  }
  .card--front { top: 30px; background: var(--paper); }
  .card--back { top: 491px; background: radial-gradient(ellipse at 45% 40%, #c9cbce 0%, #9ea1a5 55%, #8c8f93 100%); }

  .brand { position: absolute; left: 70px; top: 160px; display: flex; align-items: center; gap: 16px; }
  .brand__mark { width: 34px; height: 34px; background: var(--brand-blue); }
  .brand__name { color: var(--brand-blue); font-weight: 600; font-size: 34px; line-height: 1; letter-spacing: .5px; text-transform: uppercase; }
  .brand__sub { color: var(--brand-blue); font-weight: 600; font-size: 34px; line-height: 1.05; letter-spacing: .5px; text-transform: uppercase; }

  .divider { position: absolute; left: 410px; top: 0; width: 1px; height: 330px; background: var(--divider); }

  .contact { position: absolute; left: 438px; top: 82px; color: var(--ink); }
  .contact__name { font-size: 23px; font-weight: 600; line-height: 1.1; }
  .contact__role { font-size: 13px; margin-bottom: 16px; }
  .contact__list { list-style: none; font-size: 14px; line-height: 1.55; }
  .contact__list li { display: flex; align-items: flex-start; gap: 9px; }
  .contact__list svg { width: 13px; height: 13px; margin-top: 4px; flex: none; fill: var(--brand-blue); }
  .contact__indent { padding-left: 22px; }

  .bands { position: absolute; left: 0; bottom: 0; width: 760px; height: 434px; }
  .site { position: absolute; right: 22px; bottom: 41px; color: var(--white); font-size: 13px; letter-spacing: .3px; }

  .skyline { position: absolute; left: 0; right: 0; bottom: 0; height: 300px;
    background: linear-gradient(180deg, rgba(15,75,156,0) 0%, rgba(15,75,156,.75) 45%, #0f4b9c 100%); }
</style>
</head>
<body>
<main class="canvas">

  <section class="card card--front" aria-label="Business card front">
    <div class="brand">
      <span class="brand__mark"></span>
      <div>
        <div class="brand__name">Amber Hollow</div>
        <div class="brand__sub">Productions</div>
      </div>
    </div>

    <div class="divider"></div>

    <div class="contact">
      <div class="contact__name">Daniel Reyes</div>
      <div class="contact__role">Director</div>
      <ul class="contact__list">
        <li><svg viewBox="0 0 16 16"><path d="M8 1 1 8h2v7h4v-4h2v4h4V8h2z"/></svg><span>4/18, Harbor Court Lane</span></li>
        <li class="contact__indent">Milford OR 9700</li>
        <li><svg viewBox="0 0 16 16"><path d="M3.6 1.2 6 3.6 4.6 5.8c.9 2 2.6 3.7 4.6 4.6l2.2-1.4 2.4 2.4-1.6 2.6C6.8 14 2 9.2 1 3.8z"/></svg><span>555-210-4836</span></li>
        <li><svg viewBox="0 0 16 16"><path d="M2 5h12v8H2zM4 2h8v3H4zM4 8h2v2H4zm3 0h2v2H7zm3 0h2v2h-2z"/></svg><span>555-210-4837</span></li>
        <li><svg viewBox="0 0 16 16"><path d="M1 3h14v10H1zm1.5 1.5L8 9l5.5-4.5z"/></svg><span>hello@amberhollow.example</span></li>
      </ul>
    </div>

    <svg class="bands" viewBox="0 0 760 434" aria-hidden="true">
      <polygon points="0,396 500,396 508,384 508,396 500,408 0,408" fill="var(--brand-blue)"/>
      <polygon points="0,396 505,396 497,408 0,408" fill="var(--brand-blue)"/>
      <polygon points="520,372 760,372 760,410 495,410" fill="var(--steel)"/>
    </svg>
    <div class="site">www.amberhollow.example</div>
  </section>

  <section class="card card--back" aria-label="Business card back">
    <div class="skyline" role="img" aria-label="City skyline rising above a film strip, in brand blue"></div>
  </section>

</main>
</body>
</html>
```